Photojournalism/photography business needs a simple, timeless & professional letterhead design

We need a letterhead design for photography/photojournalism business called 'qolvb', no capitals.

The letterhead needs to be:
- simple
- professional
- timeless
- easy to read
- consists of at least 2 colors to make it stands out.

We do mainly editorial photography, photo articles for various publications, travel, businesses, as well as people such as family and kids.

The final design should communicate professionalism, easy identification, attention grabbing, even if it has to be found among a stack of various papers on the clients' desks.

Target Market(s)

Various publications.

Industry/Entity Type

Business

Requirements
Must have
• Please use the logo attached.

```html
<!DOCTYPE html>
<html lang="en">
<head>
<meta charset="utf-8">
<title>qolvb stationery</title>
<link href="https://fonts.googleapis.com/css2?family=Arimo:wght@400;700&display=swap" rel="stylesheet">
<style>
  :root {
    --ink: #1d1b1c;
    --black: #000000;
    --paper: #ffffff;
    --paper-shade: #f1f1f1;
    --stage: #e6e7e7;
    --stage-light: #f4f4f4;
    --text: #3a3a3a;
  }
  * { box-sizing: border-box; margin: 0; padding: 0; }
  html, body { width: 1200px; height: 848px; overflow: hidden; }
  body {
    position: relative;
    background: radial-gradient(ellipse at 50% 40%, var(--stage-light) 0%, var(--stage) 75%);
    font-family: "Arimo", Arial, sans-serif;
    color: var(--text);
  }
  .piece { position: absolute; box-shadow: 0 1px 3px rgba(0,0,0,0.35); }
  .wordmark { position: absolute; font-weight: 700; letter-spacing: -0.5px; line-height: 1; }

  /* folder */
  .folder { left: 117px; top: 137px; width: 442px; height: 624px; background: var(--ink); }
  .folder .wordmark { left: 148px; top: 278px; font-size: 62px; color: var(--paper); }

  /* letterhead */
  .letterhead {
    left: 422px; top: 65px; width: 443px; height: 625px;
    background: linear-gradient(180deg, var(--paper) 0%, var(--paper-shade) 40%, var(--paper) 60%, var(--paper-shade) 100%);
    overflow: hidden;
  }
  .corner { position: absolute; }
  .letterhead .corner-top { left: 0; top: 0; }
  .letterhead .corner-bottom { right: 0; bottom: 0; }
  .letterhead .wordmark { left: 82px; top: 28px; font-size: 40px; color: var(--ink); }
  .tagline {
    position: absolute; font-size: 4.4px; font-weight: 700; text-transform: uppercase;
    color: var(--ink); white-space: nowrap; letter-spacing: 0.05px;
  }
  .letterhead .tagline { left: 188px; top: 47px; }
  .letter-body {
    position: absolute; left: 90px; top: 111px; width: 303px;
    font-size: 8.5px; line-height: 15px; text-align: justify;
  }
  .letter-body p + p { margin-top: 14px; }
  .letter-footer {
    position: absolute; left: 185px; bottom: 2px; font-size: 3.5px; color: #b8b8b8; white-space: nowrap;
  }

  /* envelope back */
  .envelope-back { left: 622px; top: 190px; width: 488px; height: 217px; background: var(--paper); }
  .envelope-back .flap { position: absolute; left: 0; top: 0; }

  /* envelope front */
  .envelope-front { left: 619px; top: 439px; width: 490px; height: 217px; background: var(--paper); overflow: hidden; }
  .envelope-front .corner-top { left: 0; top: 0; }
  .envelope-front .corner-bottom { right: 0; bottom: 0; }
  .envelope-front .wordmark { left: 54px; top: 28px; font-size: 42px; color: var(--ink); }
  .address-window {
    position: absolute; left: 42px; top: 108px; width: 144px; height: 58px;
    background: linear-gradient(180deg, #ffffff, #f3f3f3);
    border: 1px solid #dedede; box-shadow: 0 1px 2px rgba(0,0,0,0.2);
  }
  .envelope-front .tagline { left: 42px; top: 193px; }
</style>
</head>
<body>

  <section class="piece folder">
    <span class="wordmark">qolvb</span>
  </section>

  <section class="piece letterhead">
    <svg class="corner corner-top" width="70" height="70" viewBox="0 0 70 70" aria-hidden="true">
      <polygon points="0,0 70,0 0,70" fill="var(--ink)"/>
    </svg>
    <span class="wordmark">qolvb</span>
    <span class="tagline">Lorem ipsum dolor sit amet, consectetuer adipiscing elit. Nam cursus. Morbi ut</span>
    <div class="letter-body">
      <p>Lorem ipsum dolor sit amet, consectetuer adipiscing elit. Nam cursus. Morbi ut mi. Nullam enim leo, egestas id, condimentum at, laoreet mattis, massa. Sed eleifend nonummy diam. Praesent mauris ante, elementum et, bibendum at, posuere sit amet, nibh. Duis tincidunt lectus quis dui viverra vestibulum. Suspendisse vulputate aliquam dui. Nulla elementum dui ut augue. Aliquam vehicula mi at mauris. Maecenas placerat, nisl at consequat rhoncus, sem nunc gravida justo, quis eleifend arcu velit quis lacus. Morbi magna magna, tincidunt a, mattis non, imperdiet vitae, tellus. Sed odio est, auctor ac, sollicitudin in, consequat vitae, orci. Fusce id felis. Vivamus sollicitudin metus</p>
      <p>Pellentesque habitant morbi tristique senectus et netus et malesuada fames ac turpis egestas. In posuere felis nec tortor. Pellentesque faucibus. Ut accumsan ultricies elit. Maecenas at justo id velit placerat molestie. Donec dictum lectus non odio. Cras a ante vitae enim iaculis aliquam. Mauris nunc quam, venenatis nec, euismod sit amet, egestas placerat, est. Pellentesque habitant morbi tristique senectus et netus et malesuada fames ac turpis egestas. Cras id elit. Integer quis urna. Ut ante enim, dapibus malesuada, fringilla eu, condimentum quis, tellus. Aenean porttitor eros vel dolor. Donec convallis pede venenatis nibh. Duis quam. Nam eget lorem a nibh volutpat.Quisque</p>
      <p>Mauris vel lacus vitae felis vestibulum volutpat. Etiam est nunc, venenatis in, tristique eu, imperdiet ac, nisl. Cum sociis natoque penatibus et magnis dis parturient montes, nascetur ridiculus mus. In iaculis facilisis massa. Etiam eu urna. Sed porta. Suspendisse quam leo, molestie sed, luctus quis, feugiat in, pede. Fusce tellus. Sed metus augue, convallis et, vehicula ut, pulvinar eu, ante. Integer orci tellus, tristique vitae, consequat nec, porta vel, lectus.</p>
    </div>
    <svg class="corner corner-bottom" width="90" height="64" viewBox="0 0 90 64" aria-hidden="true">
      <path d="M0,64 Q70,60 90,0 L90,64 Z" fill="var(--ink)"/>
    </svg>
    <span class="letter-footer">studio lane 12, harbour city, tel 555 0142</span>
  </section>

  <section class="piece envelope-back">
    <svg class="flap" width="488" height="66" viewBox="0 0 488 66" aria-hidden="true">
      <polygon points="0,0 488,0 482,66 6,66" fill="var(--black)"/>
    </svg>
  </section>

  <section class="piece envelope-front">
    <svg class="corner corner-top" width="76" height="76" viewBox="0 0 76 76" aria-hidden="true">
      <polygon points="0,0 76,0 0,76" fill="var(--ink)"/>
    </svg>
    <span class="wordmark">qolvb</span>
    <div class="address-window"></div>
    <span class="tagline">Lorem ipsum dolor sit amet, consectetuer adipiscing elit. Nam cursus. Morbi ut</span>
    <svg class="corner corner-bottom" width="105" height="102" viewBox="0 0 105 102" aria-hidden="true">
      <path d="M0,102 Q100,100 105,0 L105,102 Z" fill="var(--ink)"/>
    </svg>
  </section>

</body>
</html>
```